Trade Show Display

We need a design for a trade show pop up display. It should incorporate our colors and logo and should complement our other advertising pieces. Our primary brochure is uploaded. Also uploaded is a file with the text to be included and another file with the display dimensions.

```html
<!DOCTYPE html>
<html lang="en">
<head>
<meta charset="utf-8">
<title>Crestline Workforce Services – Trade Show Display</title>
<link rel="stylesheet" href="https://fonts.googleapis.com/css2?family=Montserrat:wght@500;600;700&display=swap">
<style>
  :root {
    --navy: #16405f;
    --navy-deep: #0f3150;
    --green: #6c9a2e;
    --green-light: #86b03c;
    --white: #ffffff;
    --paper: #f7f8f9;
    --ink: #1a3a55;
    --photo-light: #d9dde1;
    --photo-mid: #a9b3bc;
    --photo-dark: #5d6a77;
  }
  * { margin: 0; padding: 0; box-sizing: border-box; }
  html, body { width: 1196px; height: 1200px; overflow: hidden; background: var(--white); }
  body { font-family: "Montserrat", Arial, sans-serif; }
  .display { position: relative; width: 1196px; height: 1200px; background: var(--paper); overflow: hidden; }
  .display-art { position: absolute; inset: 0; }
  .brand { position: absolute; left: 70px; top: 96px; display: flex; align-items: center; gap: 18px; }
  .brand-mark { width: 46px; height: 46px; border-radius: 50%; background: var(--navy); }
  .brand-name { font-size: 34px; font-weight: 600; color: var(--navy); letter-spacing: 0.5px; line-height: 1.1; }
  .headline { position: absolute; left: 70px; top: 350px; color: var(--white); font-size: 50px; font-weight: 600; line-height: 1.18; }
  .services { position: absolute; left: 75px; top: 500px; display: grid; grid-template-columns: 262px 262px; row-gap: 25px; list-style: none; }
  .service { display: flex; align-items: center; gap: 14px; height: 56px; }
  .service-icon { width: 56px; height: 56px; flex: none; }
  .service-label { color: var(--white); font-size: 18px; font-weight: 700; line-height: 1.15; text-transform: uppercase; }
  .tagline { position: absolute; left: 75px; top: 962px; color: var(--white); font-size: 18px; font-weight: 700; line-height: 1.35; text-transform: uppercase; letter-spacing: 0.3px; }
  .call-pill { position: absolute; left: 790px; top: 1054px; width: 336px; height: 44px; border-radius: 22px; background: var(--green); color: var(--white); display: flex; align-items: center; justify-content: center; gap: 12px; font-size: 17px; font-weight: 600; letter-spacing: 0.4px; }
  .call-pill svg { width: 20px; height: 20px; }
  .contact-line { position: absolute; right: 70px; top: 1120px; color: var(--ink); font-size: 17px; font-weight: 700; text-transform: uppercase; letter-spacing: 0.2px; }
  .contact-line .divider { margin: 0 12px; }
</style>
</head>
<body>
<main class="display">
  <svg class="display-art" width="1196" height="1200" viewBox="0 0 1196 1200" aria-hidden="false">
    <defs>
      <linearGradient id="panelGradient" x1="0" y1="0" x2="1" y2="1">
        <stop offset="0" stop-color="#1d4f73"/>
        <stop offset="1" stop-color="#0f3150"/>
      </linearGradient>
      <linearGradient id="photoGradient" x1="0" y1="0" x2="1" y2="1">
        <stop offset="0" stop-color="#e4e7ea"/>
        <stop offset="0.45" stop-color="#b9c2ca"/>
        <stop offset="0.75" stop-color="#7d8a97"/>
        <stop offset="1" stop-color="#c9ced3"/>
      </linearGradient>
    </defs>
    <!-- top-right accent swoosh -->
    <path class="accent-top" d="M930 80 C1000 50 1080 38 1196 30 L1196 78 C1100 80 1020 84 930 92 Z" fill="var(--green)"/>
    <!-- divider under brand -->
    <path class="brand-rule" d="M0 224 C200 226 420 232 600 244" stroke="var(--green)" stroke-width="2" fill="none"/>
    <!-- photo area -->
    <path class="photo-area" role="img" aria-label="Photo of two business colleagues in an office reviewing a document together"
          d="M560 150 C760 122 980 108 1196 104 L1196 1000 L560 1000 Z" fill="url(#photoGradient)"/>
    <!-- green curve below panel -->
    <path class="accent-bottom" d="M0 1060 C200 1070 380 1072 560 1050 L560 1082 C380 1104 200 1110 0 1110 Z" fill="var(--green)"/>
    <!-- navy content panel -->
    <path class="content-panel" d="M0 290 L760 290 Q800 290 792 326 L610 1020 Q560 1066 500 1068 C330 1076 160 1076 0 1068 Z" fill="url(#panelGradient)"/>
    <!-- bottom rule -->
    <path class="base-rule" d="M150 1182 C500 1172 850 1172 1196 1180" stroke="var(--green)" stroke-width="3" fill="none"/>
  </svg>

  <div class="brand">
    <span class="brand-mark"></span>
    <span class="brand-name">Crestline Workforce Services</span>
  </div>

  <h1 class="headline">An Essential Part<br>of Business</h1>

  <ul class="services">
    <li class="service"><svg class="service-icon" viewBox="0 0 56 56"><circle cx="28" cy="28" r="26" fill="none" stroke="#8fb04f" stroke-width="2"/><rect x="17" y="20" width="22" height="15" rx="2" fill="none" stroke="#fff" stroke-width="2"/><circle cx="28" cy="27.5" r="3.5" fill="none" stroke="#fff" stroke-width="2"/></svg><span class="service-label">Payroll</span></li>
    <li class="service"><svg class="service-icon" viewBox="0 0 56 56"><circle cx="28" cy="28" r="26" fill="none" stroke="#8fb04f" stroke-width="2"/><circle cx="28" cy="22" r="5" fill="none" stroke="#fff" stroke-width="2"/><path d="M17 38c2-6 6-8 11-8s9 2 11 8" fill="none" stroke="#fff" stroke-width="2"/></svg><span class="service-label">Benefits<br>Management</span></li>
    <li class="service"><svg class="service-icon" viewBox="0 0 56 56"><circle cx="28" cy="28" r="26" fill="none" stroke="#8fb04f" stroke-width="2"/><path d="M18 38V30M25 38V24M32 38V27M39 38V19" stroke="#fff" stroke-width="3"/></svg><span class="service-label">Performance<br>Management</span></li>
    <li class="service"><svg class="service-icon" viewBox="0 0 56 56"><circle cx="28" cy="28" r="26" fill="none" stroke="#8fb04f" stroke-width="2"/><circle cx="28" cy="28" r="10" fill="none" stroke="#fff" stroke-width="2"/><circle cx="28" cy="28" r="3" fill="#fff"/></svg><span class="service-label">Human Resource<br>Administration</span></li>
    <li class="service"><svg class="service-icon" viewBox="0 0 56 56"><circle cx="28" cy="28" r="26" fill="none" stroke="#8fb04f" stroke-width="2"/><rect x="19" y="16" width="18" height="24" rx="2" fill="none" stroke="#fff" stroke-width="2"/><path d="M23 23h10M23 28h10M23 33h6" stroke="#fff" stroke-width="2"/></svg><span class="service-label">Cobra<br>Administration</span></li>
    <li class="service"><svg class="service-icon" viewBox="0 0 56 56"><circle cx="28" cy="28" r="26" fill="none" stroke="#8fb04f" stroke-width="2"/><circle cx="25" cy="26" r="7" fill="none" stroke="#fff" stroke-width="2"/><path d="M30 31l8 8" stroke="#fff" stroke-width="3"/></svg><span class="service-label">Talent<br>Acquisition</span></li>
    <li class="service"><svg class="service-icon" viewBox="0 0 56 56"><circle cx="28" cy="28" r="26" fill="none" stroke="#8fb04f" stroke-width="2"/><rect x="19" y="16" width="18" height="24" rx="2" fill="none" stroke="#fff" stroke-width="2"/><path d="M23 29l4 4 7-8" fill="none" stroke="#fff" stroke-width="2"/></svg><span class="service-label">Employee<br>Onboarding</span></li>
    <li class="service"><svg class="service-icon" viewBox="0 0 56 56"><circle cx="28" cy="28" r="26" fill="none" stroke="#8fb04f" stroke-width="2"/><circle cx="28" cy="28" r="11" fill="none" stroke="#fff" stroke-width="2"/><path d="M28 21v7l5 3" fill="none" stroke="#fff" stroke-width="2"/></svg><span class="service-label">Time and<br>Attendance</span></li>
    <li class="service"><svg class="service-icon" viewBox="0 0 56 56"><circle cx="28" cy="28" r="26" fill="none" stroke="#8fb04f" stroke-width="2"/><path d="M16 23l12-7 12 7zM19 25v11M25 25v11M31 25v11M37 25v11M16 39h24" fill="none" stroke="#fff" stroke-width="2"/></svg><span class="service-label">Compliance</span></li>
    <li class="service"><svg class="service-icon" viewBox="0 0 56 56"><circle cx="28" cy="28" r="26" fill="none" stroke="#8fb04f" stroke-width="2"/><rect x="16" y="20" width="24" height="16" rx="2" fill="none" stroke="#fff" stroke-width="2"/><path d="M16 25h24" stroke="#fff" stroke-width="3"/></svg><span class="service-label">Cafeteria/FSA/HRA<br>Administration</span></li>
  </ul>

  <p class="tagline">Human capital management solutions for<br>the entire employee lifecycle</p>

  <div class="call-pill">
    <span>CALL US TODAY</span>
    <svg viewBox="0 0 20 20"><circle cx="10" cy="10" r="9" fill="none" stroke="#fff" stroke-width="1.5"/><path d="M7 5.5l1.8 2.4-1 1.2c.6 1.3 1.6 2.3 2.9 2.9l1.2-1 2.4 1.8-.9 1.5c-3.8-.3-7-3.5-7.3-7.3z" fill="#fff"/></svg>
    <span>8225-555-0140</span>
  </div>

  <p class="contact-line">info@crestlineworkforce.com<span class="divider">|</span>www.crestlineworkforce.com</p>
</main>
</body>
</html>
```